Nail salon window signage design

We need new signage to be designed for our existing nail salon. The sign will be a large sticker that will stick onto the glass window at the front.

Some of the services we provide are:
Manicures
Pedicures
Velvet Gel Builder
Acrylic Nails
KVL
Lumiret
Gel Polish
You may wish to have our services listed on the sign but is not compulsory.

I have also attached our logo which can be used on the sign but is not compulsory.

I have also attached a photo of the front of our salon and the sign will be where I have outlined in yellow.

The size of the sign will be 119cm wide and 170cm high.

I am open to any nice classy design you can think of.

```html
<!DOCTYPE html>
<html lang="en">
<head>
<meta charset="utf-8">
<title>Your Nail Say Everything About You – Window Sign</title>
<link rel="stylesheet" href="https://fonts.googleapis.com/css2?family=Dancing+Script:wght@700&family=Libre+Baskerville&display=swap">
<style>
  :root {
    --backdrop: #d9d2cc;
    --glass: #cdb6a8;
    --glass-light: #e2d3c8;
    --frame-gold: #d9a57a;
    --script-pink: #f2b8bf;
    --script-pink-deep: #e79aa6;
    --cream: #f3deb8;
    --sage: #8faa6a;
    --peach: #f3c79a;
    --shadow: rgba(90, 60, 50, 0.35);
    --botanical: #b5b98e;
    --photo-skin: #e9bfa6;
    --photo-pink: #f4c6cc;
    --photo-orange: #f0955a;
  }
  * { margin: 0; padding: 0; box-sizing: border-box; }
  html, body { width: 1200px; height: 1200px; overflow: hidden; }
  body { background: var(--backdrop); position: relative; }

  .sign {
    position: absolute; left: 250px; top: 90px;
    width: 700px; height: 1020px;
    background: linear-gradient(170deg, var(--glass-light) 0%, var(--glass) 60%, #b9a196 100%);
    box-shadow: 0 20px 50px rgba(0,0,0,0.15);
  }
  .sign-frame { position: absolute; inset: 0; width: 100%; height: 100%; }

  .headline { position: absolute; left: 0; width: 100%; text-align: center; }
  .script {
    font-family: "Dancing Script", cursive; font-weight: 700;
    color: var(--script-pink);
    text-shadow: -6px 6px 8px var(--shadow);
  }
  .serif {
    font-family: "Libre Baskerville", serif;
    text-shadow: -4px 4px 6px var(--shadow);
  }
  .line-your { top: 20px; font-size: 125px; line-height: 1; left: 30px; }
  .line-nail { top: 165px; font-size: 54px; color: var(--cream); left: 20px; }
  .line-say { top: 232px; font-size: 48px; color: var(--sage); left: 20px; }
  .line-everything { top: 300px; font-size: 170px; line-height: 1.1; color: var(--script-pink); }
  .line-about { top: 518px; font-size: 70px; color: var(--peach); left: 10px; }

  .say-rays { position: absolute; left: 270px; top: 228px; width: 190px; height: 80px; }

  .botanical { position: absolute; background: var(--botanical); opacity: 0.45; border-radius: 40% 60% 50% 50%; }
  .sprig-top-right { left: 600px; top: 70px; width: 55px; height: 105px; }
  .sprig-left { left: 80px; top: 166px; width: 110px; height: 145px; }
  .sprig-right { left: 600px; top: 520px; width: 60px; height: 75px; }
  .sprig-lower-left { left: 42px; top: 628px; width: 100px; height: 185px; }

  .photo-hand-flowers {
    position: absolute; left: 190px; top: 610px; width: 510px; height: 395px;
    border-radius: 30px 0 0 30px;
    background:
      radial-gradient(circle at 25% 75%, var(--photo-pink) 0 18%, transparent 30%),
      radial-gradient(circle at 58% 88%, var(--photo-orange) 0 12%, transparent 22%),
      linear-gradient(120deg, transparent 40%, var(--photo-skin) 70%);
    opacity: 0.9;
  }
</style>
</head>
<body>
  <main class="sign">
    <svg class="sign-frame" viewBox="0 0 700 1020" aria-hidden="true">
      <path fill="none" stroke="var(--frame-gold)" stroke-width="2"
        d="M40 20 H660 Q660 40 680 40 V980 Q660 980 660 1000 H40 Q40 980 20 980 V40 Q40 40 40 20 Z"/>
    </svg>

    <div class="botanical sprig-top-right" role="img" aria-label="Line drawing of a leafy sprig"></div>
    <div class="botanical sprig-left" role="img" aria-label="Line drawing of a wheat stalk"></div>
    <div class="botanical sprig-right" role="img" aria-label="Line drawing of a small grass sprig"></div>
    <div class="botanical sprig-lower-left" role="img" aria-label="Line drawing of a flowering branch"></div>

    <h1 class="headline script line-your">Your</h1>
    <p class="headline serif line-nail">Nail</p>
    <svg class="say-rays" viewBox="0 0 190 80" aria-hidden="true">
      <g stroke="var(--sage)" stroke-width="2" stroke-linecap="round">
        <line x1="8" y1="36" x2="26" y2="38"/><line x1="20" y1="10" x2="32" y2="20"/>
        <line x1="20" y1="66" x2="32" y2="58"/>
        <line x1="182" y1="36" x2="164" y2="38"/><line x1="170" y1="10" x2="158" y2="20"/>
        <line x1="170" y1="66" x2="158" y2="58"/>
      </g>
    </svg>
    <p class="headline serif line-say">say</p>
    <p class="headline script line-everything">everything</p>
    <p class="headline serif line-about">about you</p>

    <div class="photo-hand-flowers" role="img" aria-label="Photo of a hand with sage green nails holding pink and orange flowers"></div>
  </main>
</body>
</html>
```